Divorce Lawyer print and ebook cover (Lanterns over the quiet harbor )

I need a front and back cover for my divorce and family law book. I already have a photo and title. The back cover photo is not necessary but can be interesting the Front-main cover is a must

Target Market(s)

Prospective client

Colors

Designer to choose colors to be used in the design.

Requirements
Must have
• Front photo by viewable.

```html
<!DOCTYPE html>
<html lang="en">
<head>
<meta charset="utf-8">
<title>Lanterns over the quiet harbor — Cover</title>
<link rel="stylesheet" href="https://fonts.googleapis.com/css2?family=Barlow+Condensed:wght@500;600;700&family=Montserrat:wght@700&display=swap">
<style>
  :root {
    --page-bg: #e4e8e9;
    --mist-blue: #8fa5b2;
    --mist-light: #e2e8e6;
    --forest-gold: #e9d47c;
    --leaf-green: #b6cc62;
    --tree-gray: #6f7f86;
    --road-dark: #1c262c;
    --road-mid: #3b4649;
    --road-warm: #4a4430;
    --title-white: #ffffff;
    --accent-yellow: #f4b30a;
  }
  * { margin: 0; padding: 0; box-sizing: border-box; }
  html, body {
    width: 1200px;
    height: 2220px;
    overflow: hidden;
    background: var(--page-bg);
  }
  .cover {
    position: absolute;
    left: 48px;
    top: 294px;
    width: 1104px;
    height: 1632px;
    overflow: hidden;
    box-shadow: 0 20px 50px rgba(0,0,0,0.25);
  }
  .cover-photo {
    position: absolute;
    inset: 0;
    background:
      /* dark road fading up from the bottom */
      linear-gradient(to bottom,
        rgba(28,38,44,0) 48%,
        rgba(40,50,54,0.55) 64%,
        rgba(30,38,42,0.85) 80%,
        rgba(22,30,35,0.96) 100%),
      /* warm sunlit road edge on the right */
      radial-gradient(ellipse 45% 18% at 88% 72%, rgba(200,170,80,0.55) 0%, rgba(200,170,80,0) 100%),
      /* deep tones where the figure stands */
      radial-gradient(ellipse 22% 42% at 20% 58%, rgba(20,26,34,0.75) 0%, rgba(20,26,34,0) 100%),
      /* bare grey tree tones at upper left */
      radial-gradient(ellipse 40% 35% at 10% 15%, rgba(95,112,122,0.6) 0%, rgba(95,112,122,0) 100%),
      /* glow behind the signpost */
      radial-gradient(ellipse 35% 40% at 50% 30%, rgba(236,240,236,0.9) 0%, rgba(236,240,236,0) 100%),
      /* green foliage at right */
      radial-gradient(ellipse 45% 40% at 92% 18%, var(--leaf-green) 0%, rgba(182,204,98,0) 100%),
      radial-gradient(ellipse 40% 35% at 85% 48%, rgba(233,212,124,0.9) 0%, rgba(233,212,124,0) 100%),
      linear-gradient(100deg, var(--mist-blue) 0%, #b9c7cc 30%, var(--mist-light) 50%, var(--forest-gold) 78%, #cfcf7a 100%);
  }
  .title-block {
    position: absolute;
    right: 28px;
    top: 900px;
    text-align: right;
    font-family: "Barlow Condensed", sans-serif;
    color: var(--title-white);
    font-weight: 700;
  }
  .title-main {
    display: block;
    font-weight: 700;
    font-size: 250px;
    line-height: 0.86;
    letter-spacing: -2px;
    text-shadow: 0 3px 12px rgba(0,0,0,0.35);
  }
  .title-sub {
    display: block;
    margin-top: 20px;
    font-weight: 500;
    font-size: 88px;
    line-height: 1;
    letter-spacing: 5px;
    text-shadow: 0 2px 8px rgba(0,0,0,0.35);
  }
  .title-sub .accent {
    font-weight: 700;
    color: var(--accent-yellow);
  }
  .author-name {
    position: absolute;
    left: 0; right: 0;
    bottom: 44px;
    text-align: center;
    font-family: "Montserrat", sans-serif;
    font-weight: 700;
    font-size: 62px;
    letter-spacing: 12px;
    color: var(--title-white);
  }
</style>
</head>
<body>
  <main class="cover">
    <div class="cover-photo" role="img" aria-label="Photo: a man in a dark suit seen from behind at a forked road, a signpost with two yellow direction signs, misty bare forest on the left and sunlit green trees on the right"></div>
    <h1 class="title-block">
      <span class="title-main">LANTERNS</span>
      <span class="title-sub">OVER THE <span class="accent">QUIET HARBOR</span></span>
    </h1>
    <p class="author-name">AUTHOR NAME</p>
  </main>
</body>
</html>
```